Harwell Renewal
Project: Business card design
Business card design  - Emergency Services
Business card design
Bright & Fun-filled
3871 Pelton Ave Corwin Falls, OH 45817
harwellrenewalhq@mailvista.net
I want a 24hr symbol on there I want little logos showing we do water, fire, mold, odor I want little logos for phone, email, website, location, and also one for FB. the fb is @harwellrenewalhq Bright colors, similar to logo. Black, silver, blue preferred colors.
our large logo and maybe the symbols showing we do water, fire, mold, odor

```html
<!DOCTYPE html>
<html lang="en">
<head>
<meta charset="utf-8">
<title>Harwell Renewal — Business Card</title>
<link rel="stylesheet" href="https://fonts.googleapis.com/css2?family=Montserrat:wght@400;600;800&display=swap">
<style>
  :root {
    --stage: #2b2d31;
    --navy: #1e2432;
    --navy-line: #9aa3b5;
    --white: #ffffff;
    --silver: #c9ccd3;
    --blue: #2f8fd8;
    --green: #5aa83a;
    --orange: #f08a24;
    --red: #e53935;
    --ink: #333a46;
    --muted: #6c7280;
  }
  * { box-sizing: border-box; margin: 0; padding: 0; }
  html, body { width: 1200px; height: 1023px; overflow: hidden; }
  body {
    background: var(--stage);
    font-family: "Montserrat", Arial, sans-serif;
    position: relative;
  }
  .card {
    position: absolute;
    width: 700px;
    height: 400px;
    border-radius: 6px;
    overflow: hidden;
  }
  /* Front */
  .card-front { left: 130px; top: 70px; background: var(--navy); color: var(--white); }
  .front-brand {
    position: absolute; left: 150px; top: 110px;
    display: flex; align-items: center; gap: 22px;
  }
  .brand-dot { width: 86px; height: 86px; border-radius: 50%; background: var(--blue); flex-shrink: 0; }
  .brand-name { font-weight: 800; font-size: 44px; line-height: 1.02; letter-spacing: 1px; }
  .brand-tag { font-size: 13px; letter-spacing: 5px; color: var(--silver); margin-top: 8px; font-weight: 600; }
  .front-rule {
    position: absolute; left: 60px; right: 60px; top: 262px;
    height: 1px; background: var(--navy-line);
  }
  .services {
    position: absolute; left: 0; right: 0; top: 282px;
    display: flex; justify-content: center; gap: 34px;
  }
  .service { display: flex; flex-direction: column; align-items: center; gap: 6px; }
  .service-icon {
    width: 34px; height: 34px; border: 1.5px solid var(--white); border-radius: 50%;
    display: flex; align-items: center; justify-content: center;
  }
  .service-label { font-size: 9px; letter-spacing: 1.5px; color: var(--silver); }
  /* Back */
  .card-back { left: 370px; top: 560px; background: var(--white); color: var(--ink); }
  .roof-art {
    position: absolute; right: 0; top: 90px; width: 330px; height: 260px;
    background: linear-gradient(160deg, #eef0f3 0%, #ffffff 80%);
  }
  .back-brand {
    position: absolute; left: 40px; top: 70px;
    display: flex; align-items: center; gap: 14px;
  }
  .back-brand .brand-dot { width: 62px; height: 62px; }
  .back-brand .brand-name { font-size: 30px; color: var(--navy); }
  .back-brand .brand-tag { font-size: 10px; letter-spacing: 4px; color: var(--muted); margin-top: 4px; }
  .badge-24 { position: absolute; right: 40px; top: 28px; }
  .back-title {
    position: absolute; left: 40px; top: 200px;
    font-weight: 800; font-size: 22px; color: var(--green); letter-spacing: 1px;
  }
  .contacts { position: absolute; left: 40px; top: 240px; list-style: none; }
  .contacts li { display: flex; align-items: center; gap: 10px; font-size: 13px; margin-bottom: 9px; white-space: nowrap; }
  .contact-icon {
    width: 20px; height: 20px; border-radius: 50%; background: var(--orange);
    display: flex; align-items: center; justify-content: center; flex-shrink: 0;
  }
  .contact-square { width: 20px; height: 20px; background: var(--blue); flex-shrink: 0; border-radius: 3px; }
</style>
</head>
<body>

<section class="card card-front">
  <div class="front-brand">
    <div class="brand-dot"></div>
    <div>
      <div class="brand-name">HARWELL<br>RENEWAL</div>
      <div class="brand-tag">WATER · FIRE · MOLD</div>
    </div>
  </div>
  <div class="front-rule"></div>
  <div class="services">
    <div class="service">
      <div class="service-icon"><svg width="16" height="16" viewBox="0 0 16 16"><path d="M8 1 C8 1 3 7 3 10 a5 5 0 0 0 10 0 C13 7 8 1 8 1Z" fill="#fff"/></svg></div>
      <span class="service-label">WATER</span>
    </div>
    <div class="service">
      <div class="service-icon"><svg width="16" height="16" viewBox="0 0 16 16"><path d="M7 1 C8 4 4 6 4 10 a4 4 0 0 0 8 0 C12 8 11 6 10 5 C10 7 9 8 8.5 8 C9.5 5 8 3 7 1Z" fill="#fff"/></svg></div>
      <span class="service-label">FIRE</span>
    </div>
    <div class="service">
      <div class="service-icon"><svg width="16" height="16" viewBox="0 0 16 16"><circle cx="5" cy="6" r="2.2" fill="#fff"/><circle cx="11" cy="5" r="1.8" fill="#fff"/><circle cx="8" cy="11" r="2.5" fill="#fff"/></svg></div>
      <span class="service-label">MOLD</span>
    </div>
    <div class="service">
      <div class="service-icon"><svg width="16" height="16" viewBox="0 0 16 16" fill="none" stroke="#fff" stroke-width="1.5" stroke-linecap="round"><path d="M4 13 C2 10 6 8 4 5 M8 13 C6 10 10 8 8 5 M12 13 C10 10 14 8 12 5"/></svg></div>
      <span class="service-label">ODOR</span>
    </div>
  </div>
</section>

<section class="card card-back">
  <div class="roof-art" role="img" aria-label="Faint house roof illustration"></div>
  <div class="back-brand">
    <div class="brand-dot"></div>
    <div>
      <div class="brand-name">HARWELL<br>RENEWAL</div>
      <div class="brand-tag">WATER · FIRE · MOLD</div>
    </div>
  </div>
  <svg class="badge-24" width="86" height="86" viewBox="0 0 86 86" role="img" aria-label="24 hour service">
    <circle cx="43" cy="43" r="36" fill="#fff" stroke="#2f8fd8" stroke-width="5"/>
    <path d="M43 7 A36 36 0 0 1 79 43" fill="none" stroke="#5aa83a" stroke-width="5"/>
    <path d="M7 43 A36 36 0 0 1 20 15" fill="none" stroke="#f08a24" stroke-width="5"/>
    <text x="43" y="47" text-anchor="middle" font-family="Montserrat, Arial, sans-serif" font-weight="800" font-size="26" fill="#e53935">24</text>
    <text x="43" y="61" text-anchor="middle" font-family="Montserrat, Arial, sans-serif" font-weight="600" font-size="9" fill="#2f8fd8">HOURS</text>
  </svg>
  <h1 class="back-title">HARWELL RENEWAL</h1>
  <ul class="contacts">
    <li><span class="contact-icon"><svg width="10" height="10" viewBox="0 0 10 10"><path d="M2 1 L4 1 L5 3.5 L3.8 4.5 C4.5 6 5 6.5 6.5 7.2 L7.5 6 L10 7 L10 9 C5 10 0 5 1 1Z" fill="#fff"/></svg></span>(555) 014-2290</li>
    <li><span class="contact-icon"><svg width="10" height="10" viewBox="0 0 10 10"><rect x="1" y="2" width="8" height="6" fill="none" stroke="#fff" stroke-width="1.2"/><path d="M1 2 L5 5.5 L9 2" fill="none" stroke="#fff" stroke-width="1.2"/></svg></span>harwellrenewalhq@mailvista.net</li>
    <li><span class="contact-icon"><svg width="10" height="10" viewBox="0 0 10 10"><path d="M5 0.5 a3.2 3.2 0 0 1 3.2 3.2 C8.2 6 5 9.5 5 9.5 C5 9.5 1.8 6 1.8 3.7 A3.2 3.2 0 0 1 5 0.5Z" fill="#fff"/><circle cx="5" cy="3.7" r="1.2" fill="#f08a24"/></svg></span>3871 Pelton Ave Corwin Falls, OH 45817</li>
    <li><span class="contact-square"></span>@harwellrenewalhq</li>
  </ul>
</section>

</body>
</html>
```